Business Card Design

Harbourline Recruitment is a specialist financial services recruitment company and implementation partner

Industry/Entity Type

Business

Contact Information for Business Card

Tom Ashford
Harbourline Recruitment Ltd
e:tom.ashford@harbourline-staffing.com
m:07834 206 148
m:07712 438 560
s: tommashford

```html
<!DOCTYPE html>
<html lang="en">
<head>
<meta charset="utf-8">
<title>Harbourline Recruitment – Business Card</title>
<link rel="stylesheet" href="https://fonts.googleapis.com/css2?family=Open+Sans:wght@400;700&display=swap">
<style>
  :root {
    --stage: #e4e4e2;
    --card-dark: #2b2b2d;
    --card-dark-hi: #4a4a4d;
    --teal: #1fb8ad;
    --ink: #333333;
    --ink-soft: #555555;
    --paper: #ffffff;
  }
  * { box-sizing: border-box; margin: 0; padding: 0; }
  html, body { width: 1200px; height: 913px; overflow: hidden; }
  body {
    background: var(--stage);
    font-family: "Open Sans", Arial, sans-serif;
    position: relative;
  }
  .card {
    position: absolute;
    width: 540px;
    height: 309px;
    border-radius: 4px;
    overflow: hidden;
    box-shadow: 0 10px 24px rgba(0,0,0,.25);
  }
  .card--front {
    left: 50px; top: 110px;
    background: linear-gradient(135deg, var(--card-dark-hi) 0%, var(--card-dark) 60%, #1f1f21 100%);
  }
  .card--back {
    left: 610px; top: 494px;
    background: linear-gradient(135deg, var(--card-dark-hi) 0%, var(--card-dark) 70%);
  }
  .rule {
    position: absolute; left: 0; right: 0;
    height: 4px; background: var(--teal);
  }
  .card--front .rule--top { top: 44px; }
  .card--front .rule--bottom { bottom: 44px; }

  .brand {
    position: absolute;
    display: flex; align-items: center; gap: 12px;
  }
  .brand__mark {
    width: 44px; height: 44px; border-radius: 50%;
    background: var(--teal); flex: none;
  }
  .brand__name {
    font-weight: 700; font-size: 19px; line-height: 1.1;
    color: var(--teal); letter-spacing: .5px; text-transform: uppercase;
  }
  .card--front .brand { left: 50%; top: 50%; transform: translate(-50%, -50%); }

  .panel {
    position: absolute; left: 0; right: 0; top: 52px; bottom: 52px;
    background: var(--paper);
  }
  .card--back .rule--top { top: 52px; }
  .card--back .rule--bottom { bottom: 52px; }
  .card--back .brand { left: 28px; top: 50%; transform: translateY(-50%); }
  .card--back .brand__name { font-size: 16px; }

  .contact {
    position: absolute; left: 262px; top: 72px; width: 260px;
    color: var(--ink);
  }
  .contact__name {
    font-size: 17px; letter-spacing: .5px; text-transform: uppercase;
    padding-bottom: 6px; border-bottom: 1px solid var(--teal);
    margin-bottom: 12px; color: var(--ink-soft);
  }
  .contact__name strong { color: var(--ink); }
  .contact__row {
    display: flex; align-items: center; gap: 10px;
    font-size: 10px; line-height: 1.35; color: var(--ink-soft);
    margin-bottom: 10px;
  }
  .contact__icon {
    width: 24px; height: 20px; border-radius: 3px;
    background: var(--teal); flex: none;
    display: flex; align-items: center; justify-content: center;
  }
</style>
</head>
<body>

<section class="card card--front" aria-label="Card front">
  <div class="rule rule--top"></div>
  <div class="brand">
    <span class="brand__mark"></span>
    <span class="brand__name">Harbourline<br>Recruitment Ltd</span>
  </div>
  <div class="rule rule--bottom"></div>
</section>

<section class="card card--back" aria-label="Card back">
  <div class="panel"></div>
  <div class="rule rule--top"></div>
  <div class="rule rule--bottom"></div>

  <div class="brand">
    <span class="brand__mark"></span>
    <span class="brand__name">Harbourline<br>Recruitment Ltd</span>
  </div>

  <div class="contact">
    <p class="contact__name"><strong>Tom</strong> Ashford</p>
    <div class="contact__row">
      <span class="contact__icon">
        <svg width="12" height="12" viewBox="0 0 24 24"><path fill="#fff" d="M6.6 10.8a15 15 0 0 0 6.6 6.6l2.2-2.2c.3-.3.7-.4 1-.2 1.1.4 2.3.6 3.6.6.6 0 1 .4 1 1V20c0 .6-.4 1-1 1A17 17 0 0 1 3 4c0-.6.4-1 1-1h3.5c.6 0 1 .4 1 1 0 1.3.2 2.5.6 3.6.1.3 0 .7-.2 1z"/></svg>
      </span>
      <span>07834 206 148<br>07712 438 560</span>
    </div>
    <div class="contact__row">
      <span class="contact__icon">
        <svg width="12" height="12" viewBox="0 0 24 24" fill="none" stroke="#fff" stroke-width="2"><circle cx="12" cy="12" r="9"/><path d="M3 12h18M12 3c3 3 3 15 0 18M12 3c-3 3-3 15 0 18"/></svg>
      </span>
      <span>harbourline-staffing.com<br>tom.ashford@harbourline-staffing.com</span>
    </div>
    <div class="contact__row">
      <span class="contact__icon"></span>
      <span>tommashford</span>
    </div>
  </div>
</section>

</body>
</html>
```